High Tech Real Estate Startup needs a business card

We are developing an innovative real estate marketing product based around advanced search and virtual reality.

We talk to people, we need business cards.

Target Market(s)

The target market is technology professionals and realtors.

Contact Information for Business Card

The information to be included will include

Name
Title
Phone Number
E-mail Address
www.quelzo.com

It should use simple iconography for each one of those fields.

Font styles to use
Other font styles liked:
• Co, Jubilat, Avenir

Colors

Designer to choose colors to be used in the design.

Requirements
Must have
• Clean aesthetic,
• Good use of negative space.
• It should use our company logo, shown in the attached file. It is able to use the negative of that logo (coloured font and white background) and I have attached other acceptable accent colours in a swatch file.
Should not have
• Should not be too busy
• No extraneous text (slogans, tag lines etc)

```html
<!DOCTYPE html>
<html lang="en">
<head>
<meta charset="utf-8">
<title>Quelzo Business Card</title>
<link rel="stylesheet" href="https://fonts.googleapis.com/css2?family=Montserrat:wght@400;500;600&display=swap">
<style>
  :root {
    --teal: #13b9bb;
    --paper: #ffffff;
    --ink: #4a4a4a;
    --rule: #a9a9a9;
    --backdrop: #e6e7e8;
  }
  * { margin: 0; padding: 0; box-sizing: border-box; }
  html, body {
    width: 1200px;
    height: 1134px;
    overflow: hidden;
    background: var(--backdrop);
    font-family: "Montserrat", sans-serif;
  }
  .card {
    position: absolute;
    left: 261px;
    width: 675px;
    height: 381px;
    box-shadow: 0 3px 8px rgba(0,0,0,0.18);
  }
  .card-front { top: 161px; background: var(--paper); }
  .card-back {
    top: 590px;
    background: var(--teal);
    display: flex;
    align-items: center;
    justify-content: center;
  }
  .brand-square {
    position: absolute;
    left: 491px;
    top: 56px;
    width: 140px;
    height: 138px;
    background: var(--teal);
    display: flex;
    align-items: center;
    justify-content: center;
  }
  .brand-name {
    color: var(--paper);
    font-weight: 500;
    letter-spacing: 0.5px;
  }
  .brand-square .brand-name { font-size: 23px; }
  .card-back .brand-name { font-size: 76px; letter-spacing: 1px; }
  .person-name {
    position: absolute;
    left: 46px;
    top: 206px;
    font-size: 28px;
    font-weight: 500;
    color: var(--teal);
    line-height: 1;
  }
  .person-title {
    position: absolute;
    left: 46px;
    top: 240px;
    font-size: 18px;
    color: var(--ink);
    line-height: 1;
  }
  .divider {
    position: absolute;
    left: 46px;
    top: 271px;
    width: 584px;
    height: 2px;
    background: var(--rule);
  }
  .contact {
    position: absolute;
    left: 46px;
    display: flex;
    align-items: center;
    gap: 10px;
    font-size: 16.5px;
    color: var(--ink);
    line-height: 1;
  }
  .contact-phone { top: 289px; }
  .contact-email { top: 316px; }
  .contact svg { width: 17px; height: 17px; fill: var(--teal); }
  .website {
    position: absolute;
    right: 45px;
    top: 317px;
    font-size: 16.5px;
    color: var(--ink);
    line-height: 1;
  }
  .website .accent { color: var(--teal); }
</style>
</head>
<body>
  <section class="card card-front">
    <div class="brand-square"><span class="brand-name">QUELZO</span></div>
    <div class="person-name">Dana Whitfield</div>
    <div class="person-title">President</div>
    <div class="divider"></div>
    <div class="contact contact-phone">
      <svg viewBox="0 0 24 24" aria-hidden="true"><path d="M6.6 10.8a15.2 15.2 0 0 0 6.6 6.6l2.2-2.2a1 1 0 0 1 1-.25 11.4 11.4 0 0 0 3.6.6 1 1 0 0 1 1 1V20a1 1 0 0 1-1 1A17 17 0 0 1 3 4a1 1 0 0 1 1-1h3.5a1 1 0 0 1 1 1c0 1.25.2 2.45.6 3.6a1 1 0 0 1-.25 1z"/></svg>
      <span>555 204 7180</span>
    </div>
    <div class="contact contact-email">
      <svg viewBox="0 0 24 24" aria-hidden="true"><path d="M2 5h20v2.2l-10 6.3L2 7.2z"/><path d="M2 9.4l10 6.3 10-6.3V19H2z"/></svg>
      <span>info@quelzo.com</span>
    </div>
    <div class="website">www.<span class="accent">quelzo</span>.com</div>
  </section>
  <section class="card card-back">
    <span class="brand-name">QUELZO</span>
  </section>
</body>
</html>
```